Bold Biz Card & Stationary for a Marketing Company
Cobalt Heron Marketing Solutions
Bright & Fun-filled
Linda Hollow
Owner
2417 Maple Ridge Dr
Longmont CO 80503
lindahollow@cobaltheronmarketing.example
cobaltheronmarketing.example
I want something that is unique and/or eye catching.

```html
<!DOCTYPE html>
<html lang="en">
<head>
<meta charset="utf-8">
<title>Cobalt Heron Marketing Solutions – Stationery</title>
<link href="https://fonts.googleapis.com/css2?family=Montserrat:wght@400;600&display=swap" rel="stylesheet">
<style>
  :root {
    --orange: #f08a2c;
    --orange-deep: #e7781c;
    --paper: #ffffff;
    --ink: #6b6b6b;
    --backdrop: #d9d6d2;
  }
  * { margin: 0; padding: 0; box-sizing: border-box; }
  html, body { width: 1200px; height: 365px; overflow: hidden; }
  body {
    position: relative;
    background: var(--backdrop);
    font-family: "Montserrat", Arial, sans-serif;
    color: var(--ink);
  }
  .sheet { position: absolute; background: var(--paper); overflow: hidden; box-shadow: 0 2px 6px rgba(0,0,0,.25); }
  .sheet--orange { background: var(--orange); }

  .brand { display: flex; align-items: center; gap: 4px; color: var(--orange); font-weight: 600; line-height: 1.1; }
  .brand__dot { border-radius: 50%; background: var(--orange); flex: none; }
  .brand__name { text-transform: uppercase; letter-spacing: .04em; }
  .brand__tag { display: block; font-weight: 600; letter-spacing: .08em; text-transform: uppercase; }

  .corner-arc { position: absolute; right: 0; bottom: 0; }

  .small { font-size: 3px; line-height: 1.5; color: var(--ink); }
  .small--light { color: var(--paper); }

  /* business cards */
  .card-front { left: 24px; top: 100px; width: 68px; height: 40px; }
  .card-front .brand { position: absolute; left: 6px; top: 7px; font-size: 4px; }
  .card-front .brand__dot { width: 5px; height: 5px; }
  .card-front .brand__tag { font-size: 2.4px; }
  .card-back { left: 34px; width: 74px; height: 40px; }
  .card-back--one { top: 149px; }
  .card-back--two { top: 199px; }
  .card-back .small { position: absolute; left: 6px; top: 14px; }
  .card-back .arc-white { position: absolute; right: 0; bottom: 0; }

  /* letterhead */
  .letterhead { left: 115px; top: 36px; width: 161px; height: 295px; }
  .letterhead .brand { position: absolute; left: 10px; top: 14px; font-size: 7px; }
  .letterhead .brand__dot { width: 9px; height: 9px; }
  .letterhead .brand__tag { font-size: 3.6px; }
  .letterhead .small { position: absolute; left: 10px; top: 212px; }

  /* envelopes */
  .envelope-back { left: 302px; top: 65px; width: 231px; height: 79px; }
  .envelope-back .flap { position: absolute; inset: 0; }
  .envelope-back .seal { position: absolute; left: 110px; top: 30px; width: 10px; height: 10px; border-radius: 50%; background: var(--orange); }
  .envelope-front { left: 302px; top: 161px; width: 231px; height: 151px; }
  .envelope-front .brand { position: absolute; left: 10px; top: 10px; font-size: 5px; }
  .envelope-front .brand__dot { width: 7px; height: 7px; }
  .envelope-front .brand__tag { font-size: 2.8px; }
  .envelope-front .small { position: absolute; left: 10px; top: 30px; }

  /* presentation folder */
  .folder { left: 576px; top: 19px; width: 600px; height: 331px; display: flex; }
  .folder__inside { width: 50%; height: 100%; background: var(--orange); position: relative; }
  .folder__inside .small { position: absolute; left: 130px; bottom: 14px; }
  .folder__cover { width: 50%; height: 100%; background: var(--paper); position: relative; overflow: hidden; }
  .folder__cover .brand { position: absolute; left: 110px; top: 62px; font-size: 20px; gap: 8px; }
  .folder__cover .brand__dot { width: 26px; height: 26px; }
  .folder__cover .brand__tag { font-size: 9px; margin-top: 3px; }
  .folder__cover .small { position: absolute; right: 16px; bottom: 14px; font-size: 4px; }
</style>
</head>
<body>

  <!-- business card front -->
  <div class="sheet card-front">
    <div class="brand"><span class="brand__dot"></span><span><span class="brand__name">Cobalt Heron</span><span class="brand__tag">Marketing Solutions</span></span></div>
    <svg class="corner-arc" width="30" height="30" viewBox="0 0 30 30"><path d="M30 4 A26 26 0 0 0 4 30 L12 30 A18 18 0 0 1 30 12 Z" fill="var(--orange)"/></svg>
  </div>

  <!-- business card backs -->
  <div class="sheet sheet--orange card-back card-back--one">
    <p class="small small--light">lindahollow@cobaltheronmarketing.example<br>cobaltheronmarketing.example</p>
    <svg class="arc-white" width="30" height="30" viewBox="0 0 30 30"><path d="M30 6 A24 24 0 0 0 6 30 L11 30 A19 19 0 0 1 30 11 Z" fill="var(--paper)"/></svg>
  </div>
  <div class="sheet sheet--orange card-back card-back--two">
    <p class="small small--light">Linda Hollow<br>Owner</p>
    <svg class="arc-white" width="30" height="30" viewBox="0 0 30 30"><path d="M30 6 A24 24 0 0 0 6 30 L11 30 A19 19 0 0 1 30 11 Z" fill="var(--paper)"/></svg>
  </div>

  <!-- letterhead -->
  <div class="sheet letterhead">
    <div class="brand"><span class="brand__dot"></span><span><span class="brand__name">Cobalt Heron</span><span class="brand__tag">Marketing Solutions</span></span></div>
    <p class="small">Linda Hollow<br>2417 Maple Ridge Dr<br>Longmont CO 80503<br>cobaltheronmarketing.example</p>
    <svg class="corner-arc" width="90" height="110" viewBox="0 0 90 110"><path d="M90 10 A85 85 0 0 0 5 110 L28 110 A62 62 0 0 1 90 33 Z" fill="var(--orange)"/></svg>
  </div>

  <!-- envelope back -->
  <div class="sheet envelope-back">
    <svg class="flap" width="231" height="79" viewBox="0 0 231 79"><path d="M0 0 L115.5 42 L231 0" fill="none" stroke="#e4e4e4" stroke-width="1"/></svg>
    <span class="seal"></span>
  </div>

  <!-- envelope front -->
  <div class="sheet envelope-front">
    <div class="brand"><span class="brand__dot"></span><span><span class="brand__name">Cobalt Heron</span><span class="brand__tag">Marketing Solutions</span></span></div>
    <p class="small">2417 Maple Ridge Dr<br>Longmont CO 80503</p>
    <svg class="corner-arc" width="80" height="90" viewBox="0 0 80 90"><path d="M80 8 A78 78 0 0 0 2 90 L22 90 A58 58 0 0 1 80 28 Z" fill="var(--orange)"/></svg>
  </div>

  <!-- presentation folder -->
  <div class="sheet folder">
    <div class="folder__inside">
      <p class="small small--light">cobaltheronmarketing.example</p>
    </div>
    <div class="folder__cover">
      <div class="brand"><span class="brand__dot"></span><span><span class="brand__name">Cobalt Heron</span><span class="brand__tag">Marketing Solutions</span></span></div>
      <p class="small">lindahollow@cobaltheronmarketing.example</p>
    </div>
  </div>

</body>
</html>
```